Kestrel Aid Services Banner Ad

Need a 750 x 250-pixel banner ad with the company Logo included. Please see company website at www.kestrelaidservices.com for more information.

```html
<!DOCTYPE html>
<html lang="en">
<head>
<meta charset="utf-8">
<title>Kestrel Aid Services Banner Ad</title>
<link href="https://fonts.googleapis.com/css2?family=Open+Sans:wght@400;600;700&display=swap" rel="stylesheet">
<style>
  :root {
    --navy: #245287;
    --navy-deep: #1d4576;
    --green: #5cb82e;
    --green-bright: #17b14a;
    --ribbon-blue: #1f4fa8;
    --white: #ffffff;
    --frame: #c9c9c9;
    --photo-warm: #d8b9a8;
    --photo-cool: #b7b4cf;
    --photo-dark: #5a4440;
  }
  * { margin: 0; padding: 0; box-sizing: border-box; }
  html, body { width: 1200px; height: 859px; overflow: hidden; background: var(--white); }
  body { position: relative; font-family: "Open Sans", Arial, sans-serif; }

  .banner {
    position: absolute;
    width: 750px;
    height: 250px;
    background: var(--white);
    border: 1px solid var(--frame);
    overflow: hidden;
    transform: scale(1.2);
    transform-origin: top left;
  }
  .banner--with-cta { left: 64px; top: 40px; }
  .banner--plain { left: 54px; top: 425px; }

  .banner__art { position: absolute; inset: 0; width: 750px; height: 250px; }

  .brand {
    position: absolute;
    left: 24px;
    top: 36px;
    display: flex;
    align-items: center;
    gap: 10px;
  }
  .brand__dot { width: 34px; height: 34px; border-radius: 50%; background: var(--navy); }
  .brand__name { font-size: 24px; font-weight: 700; color: var(--navy); letter-spacing: -0.2px; }

  .tagline {
    position: absolute;
    left: 34px;
    top: 114px;
    color: var(--white);
    font-size: 15.5px;
    line-height: 26px;
    font-weight: 400;
  }

  .contact {
    position: absolute;
    top: 215px;
    display: flex;
    align-items: center;
    gap: 6px;
    color: var(--navy);
    font-weight: 700;
    font-size: 18.5px;
  }
  .contact--phone { left: 9px; }
  .contact--web { left: 238px; }
  .contact svg { width: 20px; height: 20px; }

  .cta {
    position: absolute;
    right: 0;
    bottom: 0;
    width: 126px;
    height: 40px;
    background: var(--navy);
    color: var(--white);
    font-size: 15px;
    font-weight: 600;
    display: flex;
    align-items: center;
    justify-content: center;
    gap: 8px;
  }
</style>
</head>
<body>

<section class="banner banner--with-cta">
  <svg class="banner__art" viewBox="0 0 750 250" aria-hidden="false">
    <defs>
      <linearGradient id="photoTone1" x1="0" y1="0" x2="1" y2="1">
        <stop offset="0" stop-color="var(--photo-warm)"/>
        <stop offset="0.5" stop-color="#c79a8a"/>
        <stop offset="1" stop-color="var(--photo-cool)"/>
      </linearGradient>
      <linearGradient id="ribbon1" x1="0" y1="0" x2="1" y2="1">
        <stop offset="0" stop-color="var(--green-bright)"/>
        <stop offset="0.55" stop-color="var(--green-bright)"/>
        <stop offset="0.8" stop-color="var(--ribbon-blue)"/>
        <stop offset="1" stop-color="var(--green-bright)"/>
      </linearGradient>
    </defs>
    <rect x="0" y="100" width="410" height="3" fill="var(--green)"/>
    <rect x="0" y="104" width="410" height="98" fill="var(--navy)"/>
    <rect x="0" y="203" width="430" height="3" fill="var(--green)"/>
    <path role="img" aria-label="Photo of a smiling young woman leaning on her hands" d="M385 0 H750 V250 H620 C560 230 470 200 420 150 C385 110 405 50 385 0 Z" fill="url(#photoTone1)"/>
    <path d="M372 0 H386 C404 50 384 110 420 150 C470 200 560 230 622 250 H600 C540 232 455 205 405 160 C365 115 392 55 372 0 Z" fill="url(#ribbon1)"/>
  </svg>

  <div class="brand">
    <span class="brand__dot"></span>
    <span class="brand__name">Kestrel Aid Services</span>
  </div>

  <p class="tagline">Making a positive difference in<br>the lives to the individuals<br>we serve through support&nbsp; co-ordination</p>

  <div class="contact contact--phone">
    <svg viewBox="0 0 24 24"><path fill="var(--green)" d="M6.6 10.8a15.1 15.1 0 0 0 6.6 6.6l2.2-2.2c.3-.3.7-.4 1-.2 1.1.4 2.3.6 3.6.6.6 0 1 .4 1 1V20c0 .6-.4 1-1 1A17 17 0 0 1 3 4c0-.6.4-1 1-1h3.5c.6 0 1 .4 1 1 0 1.3.2 2.5.6 3.6.1.3 0 .7-.2 1z"/></svg>
    <span>609-555-0184</span>
  </div>

  <div class="contact contact--web">
    <svg viewBox="0 0 24 24" fill="none" stroke="var(--green)" stroke-width="1.6"><circle cx="12" cy="12" r="9"/><ellipse cx="12" cy="12" rx="4" ry="9"/><path d="M3 12h18M4.5 7.5h15M4.5 16.5h15"/></svg>
    <span>www.kestrelaidservices.com</span>
  </div>

  <div class="cta">
    <span>KNOW MORE</span>
    <svg width="11" height="13" viewBox="0 0 11 13"><path d="M0 0 L11 6.5 L0 13 Z" fill="var(--white)"/></svg>
  </div>
</section>

<section class="banner banner--plain">
  <svg class="banner__art" viewBox="0 0 750 250">
    <defs>
      <linearGradient id="photoTone2" x1="0" y1="0" x2="1" y2="1">
        <stop offset="0" stop-color="var(--photo-warm)"/>
        <stop offset="0.5" stop-color="#c79a8a"/>
        <stop offset="1" stop-color="var(--photo-cool)"/>
      </linearGradient>
      <linearGradient id="ribbon2" x1="0" y1="0" x2="1" y2="1">
        <stop offset="0" stop-color="var(--green-bright)"/>
        <stop offset="0.55" stop-color="var(--green-bright)"/>
        <stop offset="0.8" stop-color="var(--ribbon-blue)"/>
        <stop offset="1" stop-color="var(--green-bright)"/>
      </linearGradient>
    </defs>
    <rect x="0" y="100" width="410" height="3" fill="var(--green)"/>
    <rect x="0" y="104" width="410" height="98" fill="var(--navy)"/>
    <rect x="0" y="203" width="430" height="3" fill="var(--green)"/>
    <path role="img" aria-label="Photo of a smiling young woman leaning on her hands" d="M385 0 H750 V250 H620 C560 230 470 200 420 150 C385 110 405 50 385 0 Z" fill="url(#photoTone2)"/>
    <path d="M372 0 H386 C404 50 384 110 420 150 C470 200 560 230 622 250 H600 C540 232 455 205 405 160 C365 115 392 55 372 0 Z" fill="url(#ribbon2)"/>
  </svg>

  <div class="brand">
    <span class="brand__dot"></span>
    <span class="brand__name">Kestrel Aid Services</span>
  </div>

  <p class="tagline">Making a positive difference in<br>the lives to the individuals<br>we serve through support&nbsp; co-ordination</p>

  <div class="contact contact--phone">
    <svg viewBox="0 0 24 24"><path fill="var(--green)" d="M6.6 10.8a15.1 15.1 0 0 0 6.6 6.6l2.2-2.2c.3-.3.7-.4 1-.2 1.1.4 2.3.6 3.6.6.6 0 1 .4 1 1V20c0 .6-.4 1-1 1A17 17 0 0 1 3 4c0-.6.4-1 1-1h3.5c.6 0 1 .4 1 1 0 1.3.2 2.5.6 3.6.1.3 0 .7-.2 1z"/></svg>
    <span>609-555-0184</span>
  </div>

  <div class="contact contact--web">
    <svg viewBox="0 0 24 24" fill="none" stroke="var(--green)" stroke-width="1.6"><circle cx="12" cy="12" r="9"/><ellipse cx="12" cy="12" rx="4" ry="9"/><path d="M3 12h18M4.5 7.5h15M4.5 16.5h15"/></svg>
    <span>www.kestrelaidservices.com</span>
  </div>
</section>

</body>
</html>
```